Business Card- Occupational Therapist

I need business cards for Tallowood KinderMove, I am an Occupational Therapist offering child centred play therapy.
I am a sole private practitioner offering play therapy services to families in rural Great Southern region of WA, my mission statement is "helping rural children and communities thrive"
This is a new business so I am needing to promote the value of child centred play therapy within the community, and my referrers (target audience) will be: rural GPs (doctors), child health nurse, schools, disability providers, child protection workers etc) but also the families of young children in rural areas.
Target Market(s)
Families of children
Referrers (Doctors, child health nurse, schools, disability providers, child protection workers)
Industry/Entity Type
Mental Health
Contact Information for Business Card
Mira Toveland
Occupational Therapist
Phone: 0487 552 019
Email: mira@tkmove.com.au
PO Box 71 | BRENNARUP WA 6412
Requirements
Must have
- Include Tallowood KinderMove logo and my contact details.
Include my credentials as an Occupational Therapist and Child Centred Play Therapist
Nice to have
- "Play is a child's language and toys are their words" Delbert Quorin

```html
<!DOCTYPE html>
<html lang="en">
<head>
<meta charset="utf-8">
<title>Tallowood KinderMove – Business Card</title>
<link href="https://fonts.googleapis.com/css2?family=Comfortaa:wght@400&family=Poppins:wght@400;500;600;700&family=Playfair+Display:wght@700&display=swap" rel="stylesheet">
<style>
  :root {
    --purple: #6a1f63;
    --green: #24a84a;
    --green-soft: #7fcf8f;
    --white: #ffffff;
    --ink: #1b1b1b;
    --backdrop: #c9ccd0;
  }
  * { box-sizing: border-box; margin: 0; padding: 0; }
  html, body { width: 1200px; height: 900px; overflow: hidden; }
  body {
    background: var(--backdrop);
    font-family: "Poppins", sans-serif;
    position: relative;
  }
  .card {
    position: absolute;
    top: 135px;
    width: 380px;
    height: 630px;
    overflow: hidden;
    box-shadow: 0 12px 30px rgba(0,0,0,0.18);
  }
  .card--front { left: 180px; }
  .card--back { left: 640px; }
  .card__bg { position: absolute; inset: 0; }
  .brand {
    position: absolute;
    top: 62px;
    left: 0;
    width: 100%;
    text-align: center;
    font-family: "Comfortaa", sans-serif;
    font-weight: 400;
    font-size: 34px;
    line-height: 1.2;
  }
  .card--front .brand { color: var(--ink); }
  .card--back .brand { color: var(--white); }
  .brand__dot {
    display: block;
    width: 70px;
    height: 70px;
    margin: 26px auto 0;
    border-radius: 50%;
    background: var(--green);
  }
  .contact {
    position: absolute;
    top: 378px;
    left: 0;
    width: 100%;
    text-align: center;
    color: var(--white);
  }
  .contact__name { font-weight: 700; font-size: 26px; line-height: 1.2; }
  .contact__role { color: var(--green); font-size: 15px; font-weight: 500; line-height: 1.45; }
  .contact__icons {
    display: flex;
    align-items: center;
    justify-content: center;
    gap: 10px;
    margin: 16px 0 14px;
  }
  .contact__rule { width: 44px; height: 2px; background: var(--green); }
  .contact__icon {
    width: 24px; height: 24px; border-radius: 50%;
    background: var(--green);
    display: flex; align-items: center; justify-content: center;
  }
  .contact__line { font-size: 15.5px; line-height: 1.75; }
  .quote {
    position: absolute;
    top: 392px;
    left: 30px;
    width: 320px;
    text-align: center;
    color: var(--white);
  }
  .quote__mark {
    font-family: "Playfair Display", serif;
    font-weight: 700;
    font-size: 64px;
    line-height: 1;
    color: var(--green-soft);
    height: 40px;
    overflow: hidden;
  }
  .quote__text { font-size: 17px; font-weight: 600; line-height: 1.5; margin-top: 6px; }
  .quote__author { font-size: 13px; font-weight: 400; margin: 4px 0 10px; }
</style>
</head>
<body>

  <section class="card card--front" aria-label="Business card front">
    <svg class="card__bg" viewBox="0 0 380 630" width="380" height="630" aria-hidden="true">
      <rect width="380" height="630" fill="var(--white)"/>
      <path d="M0,396 Q150,300 380,282 L380,630 L0,630 Z" fill="var(--green)"/>
      <path d="M0,414 Q150,312 380,296 L380,630 L0,630 Z" fill="var(--purple)"/>
    </svg>
    <div class="brand">Tallowood<br>KinderMove<span class="brand__dot"></span></div>
    <div class="contact">
      <p class="contact__name">Mira Toveland</p>
      <p class="contact__role">Occupational Therapist<br>Child Centred Play Therapist</p>
      <div class="contact__icons">
        <span class="contact__rule"></span>
        <span class="contact__icon">
          <svg width="13" height="13" viewBox="0 0 24 24" aria-label="Phone"><path fill="#fff" d="M6.6 10.8a15 15 0 0 0 6.6 6.6l2.2-2.2a1 1 0 0 1 1-.25 11 11 0 0 0 3.6.6 1 1 0 0 1 1 1V20a1 1 0 0 1-1 1A17 17 0 0 1 3 4a1 1 0 0 1 1-1h3.5a1 1 0 0 1 1 1 11 11 0 0 0 .6 3.6 1 1 0 0 1-.25 1z"/></svg>
        </span>
        <span class="contact__icon">
          <svg width="13" height="13" viewBox="0 0 24 24" aria-label="Email"><path fill="#fff" d="M3 5h18v14H3z"/><path d="M3 5l9 7 9-7" fill="none" stroke="#24a84a" stroke-width="2"/></svg>
        </span>
        <span class="contact__icon">
          <svg width="13" height="13" viewBox="0 0 24 24" aria-label="Location"><path fill="#fff" d="M12 2a7 7 0 0 0-7 7c0 5 7 13 7 13s7-8 7-13a7 7 0 0 0-7-7zm0 9.5a2.5 2.5 0 1 1 0-5 2.5 2.5 0 0 1 0 5z"/></svg>
        </span>
        <span class="contact__rule"></span>
      </div>
      <p class="contact__line">0487 552 019</p>
      <p class="contact__line">mira@tkmove.com.au</p>
      <p class="contact__line">PO Box 71 | BRENNARUP WA 6412</p>
    </div>
  </section>

  <section class="card card--back" aria-label="Business card back">
    <svg class="card__bg" viewBox="0 0 380 630" width="380" height="630" aria-hidden="true">
      <rect width="380" height="630" fill="var(--purple)"/>
      <path d="M0,396 Q150,300 380,282 L380,630 L0,630 Z" fill="var(--white)"/>
      <path d="M0,410 Q150,312 380,294 L380,630 L0,630 Z" fill="var(--green)"/>
    </svg>
    <div class="brand">Tallowood<br>KinderMove<span class="brand__dot"></span></div>
    <blockquote class="quote">
      <p class="quote__mark">&ldquo;</p>
      <p class="quote__text">Play is a child's language and<br>toys are their words</p>
      <p class="quote__author">&ndash; Delbert Quorin &ndash;</p>
      <p class="quote__mark">&rdquo;</p>
    </blockquote>
  </section>

</body>
</html>
```